Masonry contractor Business Card and logo

I need a business card and a little logo for a new business:
Here is the basic info - ( i will provide the real name and phone number to the selected person but this will be level of content) - or if you message me i will send it to you.
I dont have a logo but have attached a photo - it would be good to incorporate this in some form. Also there is no company name but adding an D - V would be nice.

Derek Vollmer
Masonry Specialist
482 -317 -964
87 N. Alder Rd.
Brenford , GA 40823
Specialist in brick re-pointing of historical buildings.

```html
<!DOCTYPE html>
<html lang="en">
<head>
<meta charset="utf-8">
<title>Derek Vollmer – Masonry Specialist Business Card</title>
<link rel="stylesheet" href="https://fonts.googleapis.com/css2?family=Lato:wght@400;700&display=swap">
<style>
  :root {
    --page-bg: #e4e2df;
    --card-bg: #ffffff;
    --brick-dark: #3c3c3c;
    --brick-light: #7a7a7a;
    --mark-grey: #6b6b6b;
    --text-grey: #555555;
    --name-grey: #7a7a7a;
    --rule-grey: #4a4a4a;
  }
  * { box-sizing: border-box; margin: 0; padding: 0; }
  html, body {
    width: 1200px;
    height: 900px;
    overflow: hidden;
    background: var(--page-bg);
    font-family: "Lato", sans-serif;
  }
  .stage {
    width: 1200px;
    height: 900px;
    display: flex;
    flex-direction: column;
    align-items: center;
    justify-content: center;
    gap: 40px;
  }
  .card {
    position: relative;
    width: 680px;
    height: 389px;
    background: var(--card-bg);
    box-shadow: 0 6px 18px rgba(0,0,0,0.18);
    overflow: hidden;
  }
  .brick-course {
    position: absolute;
    left: 0;
    width: 100%;
    background: linear-gradient(90deg, var(--brick-dark), var(--brick-light) 50%, var(--brick-dark));
  }
  .card-front .brick-course.top { top: 0; height: 40px; }
  .card-front .brick-course.bottom { bottom: 0; height: 40px; }
  .card-back .brick-course.top { top: 0; height: 78px; }
  .card-back .brick-course.bottom { bottom: 0; height: 78px; }

  .monogram {
    position: absolute;
    width: 150px;
    height: 150px;
    border: 14px solid var(--mark-grey);
    border-radius: 50%;
    display: flex;
    align-items: center;
    justify-content: center;
    color: var(--mark-grey);
    font-weight: 700;
    font-size: 30px;
    letter-spacing: 1px;
  }
  .card-front .monogram { left: 265px; top: 82px; }
  .card-front .tagline {
    position: absolute;
    left: 0;
    right: 0;
    top: 292px;
    text-align: center;
    color: var(--text-grey);
    font-size: 15px;
    letter-spacing: 0.3px;
  }
  .card-back .monogram { left: 90px; top: 120px; }
  .card-back .divider {
    position: absolute;
    left: 282px;
    top: 112px;
    width: 1px;
    height: 165px;
    background: var(--rule-grey);
  }
  .card-back .contact {
    position: absolute;
    left: 302px;
    top: 114px;
    color: var(--text-grey);
    font-size: 17px;
    line-height: 1.4;
    white-space: nowrap;
  }
  .contact .name {
    color: var(--name-grey);
    font-weight: 700;
    font-size: 23px;
  }
  .contact .role { margin-bottom: 18px; }
</style>
</head>
<body>
<main class="stage">
  <section class="card card-front">
    <div class="brick-course top" role="img" aria-label="Grey brick course border"></div>
    <div class="monogram">D - V</div>
    <p class="tagline">Specialist in brick re-pointing of historical buildings.</p>
    <div class="brick-course bottom" role="img" aria-label="Grey brick course border"></div>
  </section>

  <section class="card card-back">
    <div class="brick-course top" role="img" aria-label="Grey brick course border"></div>
    <div class="monogram">D - V</div>
    <div class="divider"></div>
    <div class="contact">
      <p class="name">Derek Vollmer</p>
      <p class="role">Masonry Specialist</p>
      <p>87 N. Alder Rd.</p>
      <p>Brenford , GA 40823</p>
    </div>
    <div class="brick-course bottom" role="img" aria-label="Grey brick course border"></div>
  </section>
</main>
</body>
</html>
```